Create a new website for "The Arcade at Fernbrook"

I need a website for a shopping center in Atlanta USA. I want a classy high end look with high end motion videos (which I will provide).
The purpose of website is to attract new tenants to fill up vacant office spaces we have.
we will highlight existing cool stores and advertise that this is a cool place to start a new tenants business or office . ideally IT businesses in Alpharetta city in Georgia state in USA

Target Market(s)

commercial office tenants

Industry/Entity Type

Real Estate

Contact Information for Business Card

classy high end design
Arcade at Fernbrook
address:
2870 Briarwell Pkwy
Linwood Falls GA 30871

Logo Text

I am open. Anything that attracts new IT tech tenants to lease up shopping center/ office space

Coding

Coded - Design and coding required

Number of Pages Required

5+ page

Requirements
Must have
• easy to browse

here is a link to some photos. i will provide videos shortly

http://www.tomsereph.com/2014/04/Building-Photos-3/n-5N2dg/
Nice to have
• please look at some of mall websites i like. Moving videos and images on home page

I really like this one: https://www.plazaatcresthollow.com/

others are

https://lindorecenter.com/

https://www.discoverbrisket.com/

```html
<!DOCTYPE html>
<html lang="en">
<head>
<meta charset="utf-8">
<title>Arcade at Fernbrook</title>
<link href="https://fonts.googleapis.com/css2?family=Montserrat:wght@400;500;600;700&family=Playfair+Display:ital,wght@0,400;1,400&display=swap" rel="stylesheet">
<style>
:root{
  --blush:#e8e0df;
  --ink:#222222;
  --text:#3a3a3a;
  --muted:#8a8a8a;
  --white:#ffffff;
  --night:#141414;
  --rule:#d9d2d1;
}
*{margin:0;padding:0;box-sizing:border-box}
html,body{width:1200px;height:3367px;overflow:hidden}
body{position:relative;background:var(--white);font-family:'Montserrat',sans-serif;color:var(--text)}
.abs{position:absolute}
.serif{font-family:'Playfair Display',serif;font-style:italic;text-transform:uppercase;color:var(--ink);letter-spacing:.2em;font-weight:400}
.rule{position:absolute;height:2px;background:var(--ink)}
.copy{font-size:10px;line-height:16.4px;color:var(--text)}
.btn{position:absolute;display:flex;align-items:center;justify-content:center;background:var(--blush);color:var(--ink);font-size:11px;font-weight:700;letter-spacing:.25em;text-transform:uppercase}
.photo{position:absolute}

.topbar{left:0;top:0;width:1200px;height:31px;background:var(--blush)}
.topbar .addr{left:203px;top:10px;font-size:9px;color:var(--ink)}
.social{display:flex;gap:14px}
.social span{width:9px;height:9px;border-radius:50%;background:var(--ink);display:block}
.topbar .social{position:absolute;left:935px;top:11px}

.brand{left:0;top:50px;width:1200px;text-align:center;font-family:'Playfair Display',serif;font-size:23px;letter-spacing:.2em;text-transform:uppercase;color:var(--ink)}
.nav{left:0;top:94px;width:1200px;height:32px;border-top:1px solid var(--rule);border-bottom:1px solid var(--rule)}
.nav a{position:absolute;top:10px;font-size:10px;color:var(--ink);text-decoration:none;text-transform:uppercase;letter-spacing:.03em}

.hero{left:0;top:126px;width:1200px;height:555px;background:linear-gradient(180deg,#6d7688 0%,#c9c6c2 40%,#b8a98d 70%,#5a5550 100%)}
.hero-title{left:0;top:180px;width:1200px;text-align:center;color:var(--white);font-size:38px;line-height:40px;letter-spacing:.2em}
.hero-copy{left:340px;top:274px;width:520px;text-align:center;color:var(--white);font-size:9.5px;line-height:17px}

.tile-text{left:337px;top:1137px;width:230px}
.tile-text h3{color:var(--white);font-size:15px;line-height:17px;letter-spacing:.18em}
.tile-text p{margin-top:20px;color:var(--white);font-size:10px;line-height:16.5px}

.feature-list{left:712px;top:1816px;width:290px;list-style:none}
.feature-list li{position:relative;padding-left:16px;font-size:10px;line-height:16.5px;color:var(--text);margin-bottom:16px}
.feature-list li::before{content:"";position:absolute;left:0;top:6px;width:5px;height:5px;border-radius:50%;background:var(--ink)}

.post-label{font-size:9px;color:var(--muted);text-transform:uppercase}
.post-title{font-size:13.5px;line-height:17px;letter-spacing:.18em;margin-top:8px}

.contact{left:0;top:2643px;width:1200px;height:436px;background:var(--blush)}
.field{position:absolute;background:var(--white);font-size:9px;color:var(--muted);text-transform:uppercase;padding:13px 14px}
.submit{background:var(--ink);color:var(--white)}

.footer{left:0;top:3079px;width:1200px;height:288px;background:var(--night);color:var(--white)}
.footer h4{position:absolute;top:64px;font-family:'Playfair Display',serif;font-style:italic;font-weight:400;font-size:14px;letter-spacing:.22em;text-transform:uppercase;color:var(--white)}
.footer .links{position:absolute;top:102px;list-style:none;font-size:10px;line-height:19px}
.footer .hours{position:absolute;left:703px;top:102px;font-size:10px;line-height:19px}
.footer .social{position:absolute;left:899px;top:105px}
.footer .social span{background:var(--white)}
.footer .base{position:absolute;left:0;top:245px;width:1200px;border-top:1px solid #2c2c2c}
.footer .legal{position:absolute;left:0;top:263px;width:1200px;text-align:center;font-size:9px;color:#8d8d8d;word-spacing:2px}
.footer .legal i{font-style:normal;margin:0 22px}
</style>
</head>
<body>

<div class="abs topbar">
  <div class="abs addr">2870 Briarwell Pkwy, Linwood Falls GA 30871</div>
  <div class="social" aria-label="Social links"><span></span><span></span><span></span></div>
</div>

<div class="abs brand">Arcade at Fernbrook</div>
<nav class="abs nav">
  <a style="left:401px">Home</a>
  <a style="left:477px">About Us</a>
  <a style="left:572px">Spaces</a>
  <a style="left:655px">Blog</a>
  <a style="left:728px">Chat With Us</a>
</nav>

<section class="abs hero" role="img" aria-label="Atrium interior with curved staircase and iron railings">
  <h1 class="abs serif hero-title">Lorem Ipsum Dolor<br>Sit Amet</h1>
  <p class="abs hero-copy">Lorem ipsum dolor sit amet, consectetur adipiscing elit, sed do eiusmod tempor incididunt ut labore et dol ore magna aliqua. Ut enim ad minim veniam, quis nostrud exercitation ullamco laboris nisi ut.</p>
  <div class="btn" style="left:512px;top:327px;width:174px;height:41px">Chat With Us</div>
</section>

<div class="rule" style="left:216px;top:755px;width:41px"></div>
<h2 class="abs serif" style="left:216px;top:765px;font-size:29px;line-height:32px">Lorem Ipsum<br>Dolor Sit Amet</h2>
<p class="abs copy" style="left:610px;top:765px;width:395px;font-size:9.6px">Duis aute irure dolor in reprehenderit in voluptate velit esse cillum dolore eu fug iat nulla pariatur. Excepteur sint occaecat cupidatat non proident, sunt in culpa q ui officia deserunt mollit anim id est laborum. Sed ut perspiciatis unde omnis iste natus error sit voluptatem accusantium doloremque laudantium, totam .</p>

<div class="photo" style="left:0;top:937px;width:289px;height:314px;background:linear-gradient(180deg,#3f7fd4 0%,#dfe3e6 45%,#8c8c8c 80%,#8a3b24 100%)" role="img" aria-label="Center exterior with parked cars"></div>
<div class="photo" style="left:303px;top:890px;width:289px;height:393px;background:linear-gradient(180deg,#d9d6cf 0%,#a88e55 35%,#3d3127 70%,#1c1714 100%)" role="img" aria-label="Vacant office suite with glass doors"></div>
<div class="abs tile-text">
  <h3 class="serif">Lorem Ipsum<br>Dolor Sit Amet</h3>
  <p>Duis aute irure dolor in reprehenderit in voluptate velit esse cillum dolore eu fug iat nulla pariatur. Excepteur sint ui offi.</p>
</div>
<svg class="abs" style="left:535px;top:1248px" width="24" height="12" viewBox="0 0 24 12"><path d="M0 6H22M17 1L22 6L17 11" stroke="#fff" stroke-width="1.2" fill="none"/></svg>
<div class="photo" style="left:606px;top:937px;width:291px;height:314px;background:linear-gradient(180deg,#f1efec 0%,#e9e6e4 30%,#c23c78 60%,#b43a6e 100%)" role="img" aria-label="Empty retail unit with pink walls"></div>
<div class="photo" style="left:910px;top:937px;width:290px;height:314px;background:linear-gradient(135deg,#3b3b3b 0%,#e9dcc4 45%,#e4d3b4 100%)" role="img" aria-label="Curved stone staircase with iron railing"></div>

<div class="rule" style="left:579px;top:1353px;width:41px"></div>
<h2 class="abs serif" style="left:0;top:1360px;width:1200px;text-align:center;font-size:30px">Sed Ut Perspiciatis</h2>
<p class="abs copy" style="left:290px;top:1421px;width:620px;text-align:center;font-size:9.6px">Duis aute irure dolor in reprehenderit in voluptate velit esse cillum dolore eu fugiat nulla pariatur. Excepteur sint occaecat cupidatat non proident, sunt in culpa qui officia deserunt mollit anim id est laborum. Sed ut perspiciatis unde omnis ist.</p>
<div class="btn" style="left:512px;top:1480px;width:174px;height:41px">Contact Us</div>

<div class="photo" style="left:0;top:1597px;width:647px;height:458px;background:linear-gradient(160deg,#d8dde0 0%,#eef0f1 40%,#b9b3ab 75%,#6b5a48 100%)" role="img" aria-label="Team meeting around a conference table, video thumbnail"></div>
<svg class="abs" style="left:283px;top:1786px" width="80" height="80" viewBox="0 0 80 80"><circle cx="40" cy="40" r="40" fill="#fff"/><path d="M34 30L50 40L34 50Z" fill="#111"/></svg>
<div class="rule" style="left:712px;top:1627px;width:42px"></div>
<h2 class="abs serif" style="left:712px;top:1636px;font-size:29px;line-height:32px">Duis Aute<br>Irure Dolor<br>In Reprehen</h2>
<p class="abs copy" style="left:712px;top:1766px;width:290px">Duis aute irure dolor in reprehenderit in voluptate velit esse cillum dolore eu fug iat nulla pariatur.</p>
<ul class="abs feature-list">
  <li>Sed ut perspiciatis unde omnis iste natus error sit voluptatem accusantium doloremque laudantium.</li>
  <li>Totam rem aperiam, eaque ipsa quae ab illo inventore veritatis et quasi architecto beatae vitae dicta</li>
  <li>Sunt explicabo. Nemo enim ipsam voluptatem quia voluptas sit aspernatur aut odit aut fugit.</li>
</ul>
<div class="btn" style="left:712px;top:1983px;width:175px;height:42px">Learn More</div>

<div class="rule" style="left:579px;top:2121px;width:41px"></div>
<h2 class="abs serif" style="left:0;top:2128px;width:1200px;text-align:center;font-size:30px">Lorem Ipsum Dolor</h2>
<div class="photo" style="left:203px;top:2211px;width:389px;height:279px;background:linear-gradient(180deg,#2a3f7a 0%,#4c5e92 40%,#d9a15a 70%,#3c3a30 100%)" role="img" aria-label="Bakery storefront at dusk"></div>
<div class="photo" style="left:606px;top:2211px;width:390px;height:279px;background:linear-gradient(180deg,#cfe0f0 0%,#4f6b3f 40%,#c9b79a 65%,#7a3a2e 85%,#6b7b4e 100%)" role="img" aria-label="Monument sign with tenant panels and landscaping"></div>
<div class="abs" style="left:203px;top:2507px;width:389px">
  <div class="post-label">Duis Aute</div>
  <div class="serif post-title">Duis aute irure dolor in repre henderit in voluptate velit esse</div>
</div>
<div class="abs" style="left:606px;top:2507px;width:390px">
  <div class="post-label">Duis Aute</div>
  <div class="serif post-title">Duis aute irure dolor in repre henderit in voluptate velit esse</div>
</div>

<section class="abs contact">
  <div class="rule" style="left:579px;top:50px;width:41px"></div>
  <h2 class="abs serif" style="left:0;top:57px;width:1200px;text-align:center;font-size:30px">Lorem Ipsum Dolor</h2>
  <p class="abs copy" style="left:290px;top:116px;width:620px;text-align:center;font-size:9.6px">Duis aute irure dolor in reprehenderit in voluptate velit esse cillum dolore eu fugiat nulla pariatur. Excepteur sint occaecat cupidatat non proident, sunt in culpa qui officia deserunt mollit anim id est laborum. Sed ut perspiciatis unde omnis ist.</p>
  <div class="field" style="left:331px;top:178px;width:265px;height:35px">Name</div>
  <div class="field" style="left:604px;top:178px;width:264px;height:35px">Email</div>
  <div class="field" style="left:331px;top:223px;width:537px;height:104px">Message</div>
  <div class="btn submit" style="left:512px;top:340px;width:174px;height:42px">Submit</div>
</section>

<footer class="abs footer">
  <h4 style="left:204px">Address</h4>
  <div class="abs" style="left:204px;top:102px;font-size:13.5px;line-height:19px">2870 Briarwell Pkwy<br>Linwood Falls GA 30871</div>
  <h4 style="left:440px">Overview</h4>
  <ul class="links" style="left:440px"><li>Home</li><li>About Us</li><li>Spaces</li><li>Blog</li><li>Chat with us</li></ul>
  <ul class="links" style="left:567px"><li>Lorem</li><li>Ipsum</li><li>Dolor sit</li><li>Amet</li><li>Consectetur</li></ul>
  <h4 style="left:703px">Hours</h4>
  <div class="hours"><b>Monday – Saturday:</b><br>9am – 8pm<br><br><b>Sunday:</b> 12pm – 6pm</div>
  <h4 style="left:899px">Follow Us</h4>
  <div class="social" aria-label="Social links"><span></span><span></span><span></span></div>
  <div class="base"></div>
  <div class="legal">© Copyright 2020 Arcade at Fernbrook<i>|</i>All Rights Reserved<i>|</i>Privacy Policy<i>|</i>Terms &amp; Conditions</div>
</footer>

</body>
</html>
```